Website for Healthy Energy Bars

I need the layout for a website that will allow customers to purchase three different energy bars. It should have a slide show of pictures on the front page and the following tabs: About, Nutrition Info, FAQ

The website colors should not conflict with the colors of the company logo. Other than that I am open to design ideas and concepts.

Target Market(s)

Health-Conscious Eaters

Industry/Entity Type

Purchase

Number of Pages Required

3 page

Requirements
Must have
• Logo and pictures of the product
Should not have
• Colors that conflict with the logo colors

```html
<!DOCTYPE html>
<html lang="en">
<head>
<meta charset="utf-8">
<title>Verdabar – Healthy Energy Bars</title>
<link href="https://fonts.googleapis.com/css2?family=Open+Sans:wght@400;600;700;800&display=swap" rel="stylesheet">
<style>
:root{
  --green:#7ab828;
  --green-dark:#5f9419;
  --maroon:#5c1930;
  --maroon-light:#7a2a4b;
  --ink:#333;
  --muted:#888;
  --line:#e2e2e2;
  --topbar:#ececec;
  --slide:#efefef;
  --footer:#353b40;
  --footer-text:#b9bec2;
  --bottom:#26292c;
  --white:#fff;
}
*{box-sizing:border-box;margin:0;padding:0}
html,body{width:720px;height:1200px;overflow:hidden}
body{font-family:"Open Sans",Arial,sans-serif;color:var(--ink);background:var(--white);font-size:9px}
.wrap{width:640px;margin:0 auto;position:relative}

.topbar{height:22px;background:var(--topbar);border-bottom:1px solid var(--line)}
.topbar .wrap{display:flex;justify-content:space-between;align-items:center;height:22px}
.account-links{display:flex;gap:22px;margin-left:120px;font-size:8px;color:#555;text-transform:uppercase}
.account-links span::before{content:"";display:inline-block;width:6px;height:6px;background:var(--green);border-radius:50%;margin-right:4px;vertical-align:middle}
.cart{font-size:8px;font-weight:700;text-transform:uppercase;color:#555}

.header{height:78px}
.header .wrap{display:flex;align-items:center;justify-content:space-between;height:78px}
.brand{display:flex;align-items:center;gap:8px}
.brand-dot{width:22px;height:22px;border-radius:50%;background:var(--green)}
.brand-name{font-size:28px;font-weight:800;color:var(--green);letter-spacing:-.5px}
.search{width:180px;height:20px;border:1px solid #ccc;background:#f7f7f7;display:flex;align-items:center;justify-content:space-between;padding:0 6px;color:#aaa;font-size:8px}
.hotline{display:flex;align-items:center;gap:8px}
.hotline-icon{width:26px;height:26px;border-radius:50%;background:var(--green);display:flex;align-items:center;justify-content:center}
.hotline small{display:block;font-size:7px;color:var(--green);font-weight:700;text-transform:uppercase}
.hotline strong{font-size:17px;color:#444;font-weight:600}

.nav{height:30px;background:var(--green)}
.nav .wrap{display:flex;height:30px}
.nav a{display:flex;align-items:center;padding:0 22px;color:var(--white);text-decoration:none;font-size:9px;font-weight:600;text-transform:uppercase;border-right:1px solid rgba(255,255,255,.35)}
.nav a.home{padding:0 14px;background:var(--green-dark)}

.slider{height:260px;background:var(--slide);position:relative}
.slider .wrap{height:260px;display:flex;align-items:center}
.slide-photo{width:330px;height:200px;margin-left:30px;border-radius:4px;background:linear-gradient(135deg,#f7f7ee 0%,#e3e8cf 45%,#c9a873 75%,#8d6a3f 100%)}
.slide-copy{margin-left:50px}
.slide-copy h2{font-size:40px;font-weight:400;color:var(--maroon);line-height:1.05}
.slide-copy p{font-size:26px;color:var(--green);margin:4px 0 14px}
.btn{display:inline-block;color:var(--white);font-size:7px;font-weight:700;text-transform:uppercase;padding:5px 10px}
.btn-green{background:var(--green)}
.btn-maroon{background:var(--maroon)}
.slide-copy .btn{padding:7px 16px;font-size:8px}
.arrow{position:absolute;top:115px;width:20px;height:30px}
.arrow.prev{left:-30px}.arrow.next{right:-30px}

.info{height:90px;display:flex}
.info-hello{flex:1;background:#f3f3f3;padding:12px 20px 0 40px}
.info-hello h3{font-size:30px;font-weight:400;color:var(--green);line-height:1}
.info-hello h3 span{font-size:12px;color:#444;font-weight:600;text-transform:uppercase}
.info-hello p{font-size:8px;line-height:1.45;color:#666;margin-top:6px;max-width:400px}
.info-delivery{width:260px;background:linear-gradient(90deg,var(--maroon) 0%,var(--maroon-light) 60%,#5d2a56 100%);padding:18px 0 0 30px;font-size:24px;line-height:1.1;text-transform:uppercase;color:var(--white)}
.info-delivery span{color:#e7a8c0}

.featured{padding-top:14px}
.featured h4{font-size:14px;font-weight:700;text-transform:uppercase;color:#333;padding-bottom:8px;border-bottom:1px solid var(--line);margin-bottom:12px}
.grid{display:grid;grid-template-columns:repeat(4,148px);gap:14px 16px}
.card-photo{height:122px;border:1px solid var(--line);display:flex;align-items:center;justify-content:center}
.card-photo div{width:96px;height:70px;border-radius:3px;background:linear-gradient(135deg,#fafaf2 0%,#e4eac9 50%,#b79363 100%)}
.price{margin-top:7px;font-size:12px;color:var(--green);font-weight:600}
.price s{font-size:7px;color:var(--muted);margin-left:3px}
.name{font-size:8px;font-weight:700;text-transform:uppercase;margin-top:2px}
.desc{font-size:7.5px;color:#777;line-height:1.35;margin-top:3px;height:31px}
.actions{display:flex;gap:4px;margin-top:5px}

.footer{position:absolute;top:1032px;left:0;width:720px;height:140px;background:var(--footer)}
.footer .wrap{display:grid;grid-template-columns:repeat(4,1fr);padding-top:18px}
.footer h5{font-size:8px;color:var(--green);text-transform:uppercase;font-weight:700;margin-bottom:7px}
.footer li{list-style:none;font-size:8px;color:var(--footer-text);line-height:1.55}
.bottombar{position:absolute;top:1172px;left:0;width:720px;height:28px;background:var(--bottom)}
.bottombar .wrap{display:flex;align-items:center;gap:10px;height:28px}
.bottombar .mini{font-size:12px;font-weight:800;color:var(--green)}
.bottombar small{font-size:7.5px;color:#999}
</style>
</head>
<body>
<div class="topbar"><div class="wrap">
  <div class="account-links"><span>Wishlist</span><span>Sign in</span><span>My account</span><span>Checkout</span></div>
  <div class="cart">Cart (0)</div>
</div></div>

<header class="header"><div class="wrap">
  <div class="brand"><div class="brand-dot"></div><div class="brand-name">Verdabar</div></div>
  <div class="search">Search here…
    <svg width="9" height="9" viewBox="0 0 10 10"><circle cx="4" cy="4" r="3" fill="none" stroke="#999" stroke-width="1.4"/><line x1="6.2" y1="6.2" x2="9" y2="9" stroke="#999" stroke-width="1.4"/></svg>
  </div>
  <div class="hotline">
    <div class="hotline-icon"><svg width="13" height="13" viewBox="0 0 24 24"><path d="M6.6 10.8a15 15 0 0 0 6.6 6.6l2.2-2.2c.3-.3.7-.4 1-.2 1.1.4 2.3.6 3.6.6.6 0 1 .4 1 1V20c0 .6-.4 1-1 1A17 17 0 0 1 3 4c0-.6.4-1 1-1h3.5c.6 0 1 .4 1 1 0 1.2.2 2.4.6 3.6.1.3 0 .7-.2 1z" fill="#fff"/></svg></div>
    <div><small>Call us free today</small><strong>1-555-010-2468</strong></div>
  </div>
</div></header>

<nav class="nav"><div class="wrap">
  <a class="home" href="#"><svg width="12" height="12" viewBox="0 0 24 24"><path d="M12 3 2 12h3v8h5v-6h4v6h5v-8h3z" fill="#fff"/></svg></a>
  <a href="#">About us</a><a href="#">Nutrition info</a><a href="#">FAQ</a><a href="#">Contact us</a>
</div></nav>

<section class="slider"><div class="wrap">
  <svg class="arrow prev" viewBox="0 0 20 30"><polyline points="14,4 5,15 14,26" fill="none" stroke="#bbb" stroke-width="2"/></svg>
  <div class="slide-photo" role="img" aria-label="Boxes of energy bars with an unwrapped bar in front"></div>
  <div class="slide-copy">
    <h2>Special<br>Offer !</h2>
    <p>Save up to 50%</p>
    <span class="btn btn-maroon">Shop now</span>
  </div>
  <svg class="arrow next" viewBox="0 0 20 30"><polyline points="6,4 15,15 6,26" fill="none" stroke="#bbb" stroke-width="2"/></svg>
</div></section>

<section class="info">
  <div class="info-hello">
    <h3>Hello! <span>Our nutrition info</span></h3>
    <p>Lorem Ipsum is simply dummy text of the printing and typesetting industry. Lorem Ipsum has been the industry's standard dummy text ever since the 1500s. Lorem Ipsum is simply dummy text of the printing and typesetting industry.</p>
  </div>
  <div class="info-delivery">Free <span>&amp;</span> Fast<br>Delivery</div>
</section>

<section class="featured"><div class="wrap">
  <h4>Featured products</h4>
  <div class="grid">
    <div class="card"><div class="card-photo"><div role="img" aria-label="Box of chocolate energy bars"></div></div><div class="price">$28.00<s>$32.00</s></div><div class="name">Boxchocolate</div><div class="desc">Lorem Ipsum is simply dummy text of the printing and typesetting industry.</div><div class="actions"><span class="btn btn-green">Add to cart</span><span class="btn btn-maroon">View</span></div></div>
    <div class="card"><div class="card-photo"><div role="img" aria-label="Single coconut energy bar"></div></div><div class="price">$10.00<s>$12.00</s></div><div class="name">Barcoconut</div><div class="desc">Lorem Ipsum is simply dummy text of the printing and typesetting industry.</div><div class="actions"><span class="btn btn-green">Add to cart</span><span class="btn btn-maroon">View</span></div></div>
    <div class="card"><div class="card-photo"><div role="img" aria-label="Box of cherry energy bars"></div></div><div class="price">$43.00<s>$48.00</s></div><div class="name">Boxcherry</div><div class="desc">Lorem Ipsum is simply dummy text of the printing and typesetting industry.</div><div class="actions"><span class="btn btn-green">Add to cart</span><span class="btn btn-maroon">View</span></div></div>
    <div class="card"><div class="card-photo"><div role="img" aria-label="Single chocolate energy bar"></div></div><div class="price">$70.00<s>$76.00</s></div><div class="name">Barchoc brat</div><div class="desc">Lorem Ipsum is simply dummy text of the printing and typesetting industry.</div><div class="actions"><span class="btn btn-green">Add to cart</span><span class="btn btn-maroon">View</span></div></div>
    <div class="card"><div class="card-photo"><div role="img" aria-label="Single cherry energy bar"></div></div><div class="price">$28.00<s>$32.00</s></div><div class="name">Barcherry brat</div><div class="desc">Lorem Ipsum is simply dummy text of the printing and typesetting industry.</div><div class="actions"><span class="btn btn-green">Add to cart</span><span class="btn btn-maroon">View</span></div></div>
    <div class="card"><div class="card-photo"><div role="img" aria-label="Box of coconut energy bars"></div></div><div class="price">$10.00<s>$12.00</s></div><div class="name">Boxcoconut</div><div class="desc">Lorem Ipsum is simply dummy text of the printing and typesetting industry.</div><div class="actions"><span class="btn btn-green">Add to cart</span><span class="btn btn-maroon">View</span></div></div>
    <div class="card"><div class="card-photo"><div role="img" aria-label="Box of cherry energy bars"></div></div><div class="price">$43.00<s>$48.00</s></div><div class="name">Boxcherry</div><div class="desc">Lorem Ipsum is simply dummy text of the printing and typesetting industry.</div><div class="actions"><span class="btn btn-green">Add to cart</span><span class="btn btn-maroon">View</span></div></div>
    <div class="card"><div class="card-photo"><div role="img" aria-label="Single coconut energy bar"></div></div><div class="price">$70.00<s>$76.00</s></div><div class="name">Barcoconut</div><div class="desc">Lorem Ipsum is simply dummy text of the printing and typesetting industry.</div><div class="actions"><span class="btn btn-green">Add to cart</span><span class="btn btn-maroon">View</span></div></div>
  </div>
</div></section>

<footer class="footer"><div class="wrap">
  <div><h5>Quick link</h5><ul><li>Home</li><li>About us</li><li>Nutrition info</li><li>FAQ</li><li>Contact us</li></ul></div>
  <div><h5>Why choose us?</h5><ul><li>Great Taste</li><li>Natural Ingredients</li><li>Fresh Stock</li><li>Fast Shipping</li><li>Secure Payment</li></ul></div>
  <div><h5>My account</h5><ul><li>My orders</li><li>My addresses</li><li>My wishlist</li><li>My account</li></ul></div>
  <div><h5>Contacts</h5><ul><li>12 Orchard Lane, Greenfield,</li><li>Anytown 10101</li><li>hello@verdabar.com</li><li>1-555-010-2468</li></ul></div>
</div></footer>
<div class="bottombar"><div class="wrap"><span class="mini">Verdabar</span><small>Copyright © 2015 Verdabar. All Rights Reserved.</small></div></div>
</body>
</html>
```